Business Card Design for Property Development Company Director

I am looking for a professional and unforgettable business card design for our Director of our Property Development Company.
Please see attached .pptx file to find out what information to include. You don't have to follow the exact format shown in the file - I am interested to see your creative flair using the information provided.

```html
<!DOCTYPE html>
<html lang="en">
<head>
<meta charset="utf-8">
<title>Calverton Property Group – Business Card</title>
<link href="https://fonts.googleapis.com/css2?family=Arimo:wght@400;700&display=swap" rel="stylesheet">
<style>
  :root {
    --backdrop: #2b2b2d;
    --paper: #f3f3f2;
    --brand-blue: #1a63c0;
    --deep-blue: #0d4691;
    --bright-blue: #2a7fe0;
    --ink-grey: #6b6b6b;
    --soft-white: #e9eef6;
  }
  * { box-sizing: border-box; margin: 0; padding: 0; }
  html, body {
    width: 1200px; height: 900px; overflow: hidden;
    background: var(--backdrop);
    font-family: "Arimo", Arial, sans-serif;
  }
  .canvas {
    width: 1200px; height: 900px;
    display: flex; justify-content: center; align-items: center; gap: 60px;
  }
  .card {
    width: 465px; height: 760px;
    border-radius: 40px;
    position: relative;
    display: flex; flex-direction: column; align-items: center;
    text-align: center;
  }
  .card--front { background: var(--paper); color: var(--ink-grey); }
  .card--back {
    background: linear-gradient(160deg, var(--bright-blue) 0%, var(--brand-blue) 45%, var(--deep-blue) 100%);
    color: var(--soft-white);
  }

  .person { margin-top: 70px; }
  .person__name { color: var(--brand-blue); font-weight: 700; font-size: 26px; letter-spacing: 1px; }
  .person__role { font-size: 15px; letter-spacing: 1px; margin-top: 4px; }

  .brand { display: flex; align-items: center; gap: 14px; }
  .brand__mark { width: 22px; height: 22px; flex: none; }
  .brand__name { font-weight: 700; font-size: 30px; line-height: 1.15; text-align: left; letter-spacing: 1px; }
  .card--front .brand { margin-top: 150px; }
  .card--front .brand__name { color: var(--brand-blue); }
  .card--front .brand__mark { background: var(--brand-blue); }
  .card--back .brand { margin-top: 170px; }
  .card--back .brand__name { color: #ffffff; }
  .card--back .brand__mark { background: #ffffff; }

  .address { color: var(--brand-blue); font-size: 20px; line-height: 1.35; margin-top: 28px; }

  .contact-icons { display: flex; gap: 34px; margin-top: 40px; }
  .contact-icons svg { width: 34px; height: 34px; }

  .contact-list { list-style: none; font-size: 21px; line-height: 1.6; margin-top: 22px; }
  .contact-list .web { color: var(--brand-blue); }

  .dash { width: 22px; height: 4px; margin-top: 26px; }
  .card--front .dash { background: var(--brand-blue); }
  .card--back .dash { background: #ffffff; }

  .licence { color: var(--brand-blue); font-size: 19px; margin-top: auto; margin-bottom: 40px; }

  .tagline { font-weight: 700; font-size: 21px; line-height: 1.45; margin-top: 22px; color: var(--soft-white); }

  .invite { margin-top: auto; margin-bottom: 60px; display: flex; flex-direction: column; align-items: center; font-size: 20px; line-height: 1.3; }
  .invite strong { font-weight: 700; letter-spacing: 0.5px; }
</style>
</head>
<body>
<main class="canvas">
  <section class="card card--front" aria-label="Card front">
    <div class="person">
      <p class="person__name">DANIEL MORROW</p>
      <p class="person__role">DIRECTOR</p>
    </div>

    <div class="brand">
      <span class="brand__mark"></span>
      <p class="brand__name">CALVERTON<br>PROPERTY GROUP</p>
    </div>

    <p class="address">No 120 Riverside Lane, Eastbrook<br>QLD 4100, Australia</p>

    <div class="contact-icons">
      <svg viewBox="0 0 34 34" aria-label="Phone">
        <circle cx="17" cy="17" r="17" fill="var(--brand-blue)"/>
        <path d="M12 10c1-1 2 0 3 2s0 2-1 3c1 2 2 3 4 4 1-1 1-2 3-1s3 2 2 3-2 2-4 2c-4-1-8-5-9-9 0-2 1-3 2-4z" fill="#fff"/>
      </svg>
      <svg viewBox="0 0 34 34" aria-label="Email">
        <circle cx="17" cy="17" r="17" fill="var(--brand-blue)"/>
        <rect x="9" y="11" width="16" height="12" rx="1" fill="#fff"/>
        <path d="M9 12l8 6 8-6" fill="none" stroke="var(--brand-blue)" stroke-width="1.5"/>
      </svg>
      <svg viewBox="0 0 34 34" aria-label="Website">
        <circle cx="17" cy="17" r="17" fill="var(--brand-blue)"/>
        <path d="M15 19l4-4M14 16l-2 2a3 3 0 0 0 4 4l2-2M20 18l2-2a3 3 0 0 0-4-4l-2 2" fill="none" stroke="#fff" stroke-width="2" stroke-linecap="round"/>
      </svg>
    </div>

    <ul class="contact-list">
      <li>0400 123 456</li>
      <li>daniel@calverton.com.au</li>
      <li class="web">www.calverton.com.au</li>
    </ul>

    <span class="dash"></span>

    <p class="licence">Real Estate Lic: 1234567 &amp; 1234568</p>
  </section>

  <section class="card card--back" aria-label="Card back">
    <div class="brand">
      <span class="brand__mark"></span>
      <p class="brand__name">CALVERTON<br>PROPERTY GROUP</p>
    </div>

    <span class="dash"></span>

    <p class="tagline">Property Development<br>&amp;<br>Site Acquisition Specialists</p>

    <div class="invite">
      <span>Ask me about our</span>
      <strong>INVESTMENT &amp; PARTNERSHIP</strong>
      <span>opportunities</span>
      <span class="dash"></span>
    </div>
  </section>
</main>
</body>
</html>
```